Game, Voice & Dedicated Server Company Needs a Business Card Design

We need a new business card design, centered around our new logo (PSD provided below).

Designs that we do like:
https://pixelmarsh.net/item/corporate-business-card/5382017?s_rank=43 (needs to be made more eye catching)

Our main areas of business are:
- Dedicated Servers
- Game Servers
- Voice Servers
- Mitigation Security Specialists

Industry/Entity Type

Business

Contact Information for Business Card

On the card: (and anything else you would suggest)
- Staff member name
- Staff member position in company
- Staff member phone number
- Staff member email
- Other / Staff member Skype
- Website link

Colors
9bcb3c
abd036

Requirements
Must have
• Design of Card:
• - Green (same green as the logo)
• - Business / Corporate design
• - Something a little different / abstract that shouts premium

```html
<!DOCTYPE html>
<html lang="en">
<head>
<meta charset="utf-8">
<title>Kestrel Hosting – Business Card</title>
<link href="https://fonts.googleapis.com/css2?family=Open+Sans:wght@400;600;700;800&display=swap" rel="stylesheet">
<style>
  :root {
    --bg-top: #2a2a2a;
    --bg-bottom: #050505;
    --white: #ffffff;
    --panel-green: #8dc63f;
    --lime: #b3f55a;
    --brand-green: #7dbb32;
    --logo-green-dark: #86c23e;
    --ink: #1a1a1a;
    --rule: rgba(255,255,255,0.35);
  }
  * { margin: 0; padding: 0; box-sizing: border-box; }
  html, body { width: 1200px; height: 900px; overflow: hidden; }
  body {
    position: relative;
    background: linear-gradient(to bottom, var(--bg-top) 0%, #151515 55%, var(--bg-bottom) 100%);
    font-family: "Open Sans", Arial, sans-serif;
  }
  .card {
    position: absolute;
    top: 306px;
    height: 271px;
    border-radius: 10px;
    overflow: hidden;
  }
  .card-front { left: 149px; width: 439px; background: var(--white); }
  .card-back { left: 608px; width: 441px; background: var(--lime); }

  .front-brand {
    position: absolute; left: 0; top: 0; width: 219px; height: 100%;
  }
  .brand-mark {
    position: absolute; left: 46px; top: 46px;
    width: 84px; height: 84px; border-radius: 50%;
    background: var(--brand-green);
  }
  .brand-name {
    position: absolute; left: 19px; top: 146px;
    font-weight: 800; font-size: 25px; line-height: 26px;
    color: var(--brand-green); letter-spacing: -0.5px;
  }

  .front-details {
    position: absolute; left: 219px; top: 0; right: 0; height: 100%;
    background: var(--panel-green); color: var(--white);
  }
  .person-name { position: absolute; left: 18px; top: 56px; font-size: 14px; font-weight: 700; }
  .person-role { position: absolute; left: 18px; top: 75px; font-size: 11.5px; }
  .rule {
    position: absolute; left: 12px; width: 132px; height: 1px;
    background: linear-gradient(to right, transparent, var(--rule), transparent);
  }
  .rule-one { top: 101px; }
  .rule-two { top: 176px; }
  .contact-list { position: absolute; left: 16px; list-style: none; font-size: 11.5px; line-height: 16px; }
  .contact-list.primary { top: 122px; }
  .contact-list.online { top: 188px; }
  .contact-list li { display: flex; align-items: center; gap: 6px; }
  .contact-list svg { width: 9px; height: 9px; fill: var(--white); flex: none; }

  .back-mark {
    position: absolute; left: 45px; top: 92px;
    width: 92px; height: 92px; border-radius: 50%;
    background: var(--logo-green-dark);
  }
  .back-name {
    position: absolute; left: 163px; top: 96px;
    font-weight: 800; font-size: 34px; line-height: 34px;
    color: var(--logo-green-dark); letter-spacing: -0.5px;
  }
</style>
</head>
<body>
  <section class="card card-front">
    <div class="front-brand">
      <div class="brand-mark"></div>
      <div class="brand-name">KESTREL<br>HOSTING</div>
    </div>
    <div class="front-details">
      <p class="person-name">Daniel Carter</p>
      <p class="person-role">Managing Director</p>
      <div class="rule rule-one"></div>
      <ul class="contact-list primary">
        <li><svg viewBox="0 0 10 10"><path d="M1 3.5Q1 1.5 3 1.5h4q2 0 2 2v1H7V3.5H3v1H1zM2 5h6l1 3.5H1z"/></svg>(044) 987 654 321</li>
        <li><svg viewBox="0 0 10 10"><path d="M1 2h8v6H1zM1.8 2.6 5 5.2l3.2-2.6v-.2H1.8z" fill-rule="evenodd"/></svg>hello@kestrelmail.net</li>
      </ul>
      <div class="rule rule-two"></div>
      <ul class="contact-list online">
        <li><svg viewBox="0 0 10 10"><circle cx="5" cy="5" r="3.5"/></svg>www.kestrelhost.net</li>
        <li><svg viewBox="0 0 10 10"><circle cx="5" cy="5" r="4"/></svg>www.chatlink.net</li>
      </ul>
    </div>
  </section>

  <section class="card card-back">
    <div class="back-mark"></div>
    <div class="back-name">KESTREL<br>HOSTING</div>
  </section>
</body>
</html>
```